The Marlowe Legal Group, P.C.
Business Cards, Stationary & Email Signature & Letterhead
Use same font as used in my logo
Ruth Benning
Attorney
2847 Tamworth Lane
Suite 3405
Kennesaw, GA 30582
ruthbenningesq@quillpost.net
www.marlowelegaloffice.com
Logo + whatever
Ai file of my logo for Stationary project

```html
<!DOCTYPE html>
<html lang="en">
<head>
<meta charset="utf-8">
<title>The Marlowe Legal Group, P.C. — Stationery</title>
<link rel="stylesheet" href="https://fonts.googleapis.com/css2?family=Libre+Baskerville&family=Open+Sans:wght@400;600&display=swap">
<style>
  :root {
    --navy: #2b3f8e;
    --navy-dark: #1f2f6e;
    --grey: #8a8d93;
    --grey-light: #d9dbe0;
    --paper: #ffffff;
    --ink: #4a4d55;
    --ink-soft: #9a9ca3;
    --backdrop: #e6e7eb;
    --brand: "Libre Baskerville", Georgia, serif;
    --body: "Open Sans", Arial, sans-serif;
  }
  * { box-sizing: border-box; margin: 0; padding: 0; }
  html, body { width: 1200px; height: 842px; overflow: hidden; }
  body { background: var(--backdrop); font-family: var(--body); color: var(--ink); position: relative; }

  .sheet { position: absolute; background: var(--paper); box-shadow: 0 2px 8px rgba(0,0,0,.12); overflow: hidden; }

  /* brand lockup */
  .brand { display: flex; align-items: center; gap: 8px; }
  .brand-dot { flex: none; border-radius: 50%; background: var(--navy); }
  .brand-name { font-family: var(--brand); font-weight: 400; color: var(--navy); line-height: 1.15; }
  .brand--light .brand-dot { background: var(--paper); }
  .brand--light .brand-name { color: var(--paper); }

  .small { font-size: 7px; line-height: 1.5; color: var(--ink); }
  .muted { color: var(--ink-soft); }

  /* letterhead */
  .letterhead { left: 40px; top: 46px; width: 340px; height: 490px; padding: 28px 30px; }
  .letterhead .brand-dot { width: 26px; height: 26px; }
  .letterhead .brand-name { font-size: 11px; }
  .letter-body { margin-top: 38px; font-size: 7px; line-height: 1.6; }
  .letter-body p { margin-bottom: 9px; }
  .signature { width: 70px; height: 22px; background: var(--grey-light); margin: 6px 0 4px; }
  .letter-footer { position: absolute; left: 30px; bottom: 34px; font-size: 6.5px; line-height: 1.5; color: var(--paper); z-index: 1; }
  .band { position: absolute; left: 0; bottom: 0; width: 100%; height: 70px; }

  /* fax sheet */
  .fax { left: 400px; top: 46px; width: 340px; height: 490px; padding: 28px 30px; }
  .fax .brand-dot { width: 26px; height: 26px; }
  .fax .brand-name { font-size: 11px; }
  .fax-title { position: absolute; right: 30px; top: 34px; font-family: var(--brand); font-size: 22px; letter-spacing: 3px; color: var(--grey); }
  .fax-table { width: 100%; margin-top: 34px; border-collapse: collapse; font-size: 8px; }
  .fax-table td { border-bottom: 1px solid var(--grey-light); padding: 7px 4px; }
  .fax-table td.label { width: 60px; color: var(--navy); font-weight: 600; }
  .fax-checks { display: flex; justify-content: space-between; margin-top: 16px; font-size: 7px; }
  .fax-checks span::before { content: ""; display: inline-block; width: 7px; height: 7px; border: 1px solid var(--grey); margin-right: 4px; vertical-align: -1px; }
  .fax-comments { margin-top: 18px; font-size: 8px; color: var(--navy); font-weight: 600; }
  .fax-lines { margin-top: 8px; height: 120px; background: repeating-linear-gradient(to bottom, transparent 0 19px, var(--grey-light) 19px 20px); }
  .fax-footer { position: absolute; left: 30px; right: 30px; bottom: 18px; border-top: 2px solid var(--navy); padding-top: 6px; font-size: 6.5px; color: var(--ink-soft); }

  /* envelope */
  .envelope-front { left: 760px; top: 46px; width: 400px; height: 230px; padding: 22px 24px; }
  .envelope-front .brand-dot { width: 24px; height: 24px; }
  .envelope-front .brand-name { font-size: 10px; }
  .envelope-front .small { margin-top: 6px; margin-left: 32px; }
  .envelope-mark { position: absolute; right: 34px; top: 26px; width: 120px; height: 120px; border-radius: 50%; background: var(--grey-light); opacity: .55; }
  .envelope-back { left: 760px; top: 306px; width: 400px; height: 230px; }
  .envelope-back svg { position: absolute; inset: 0; }
  .envelope-back .seal { position: absolute; left: 50%; top: 92px; width: 30px; height: 30px; margin-left: -15px; border-radius: 50%; background: var(--paper); }

  /* business cards */
  .card { top: 586px; width: 260px; height: 160px; }
  .card-front { padding: 18px 20px; }
  .card-front .brand-dot { width: 22px; height: 22px; }
  .card-front .brand-name { font-size: 9px; }
  .card-person { margin-top: 18px; }
  .card-person h2 { font-family: var(--brand); font-weight: 400; font-size: 11px; color: var(--navy); }
  .card-person p { font-size: 7px; color: var(--ink-soft); margin-bottom: 6px; }
  .card-stripe { position: absolute; left: 0; bottom: 0; width: 100%; height: 8px; background: var(--navy); }
  .card-back { display: flex; flex-direction: column; align-items: center; justify-content: center; gap: 10px; }
  .card-back .brand-dot { width: 30px; height: 30px; }
  .card-back .brand-name { font-size: 10px; text-align: center; }
  .card-back .web { font-size: 7px; color: var(--paper); letter-spacing: .5px; }
  .card--navy { background: var(--navy); }
  .card--grey { background: var(--grey); }
  .card-1 { left: 40px; }
  .card-2 { left: 327px; }
  .card-3 { left: 614px; }
  .card-4 { left: 900px; }
</style>
</head>
<body>

  <!-- Letterhead -->
  <section class="sheet letterhead">
    <div class="brand"><span class="brand-dot"></span><span class="brand-name">The Marlowe Legal Group, P.C.</span></div>
    <div class="letter-body">
      <p>March 4, 2024</p>
      <p>Recipient Name<br>Company Address</p>
      <p>Dear Client,</p>
      <p>Thank you for choosing our firm. We value the trust you have placed in us and will keep you informed at every step of your matter.</p>
      <p>Please call our office with any questions about your case or the documents enclosed with this letter.</p>
      <p>Sincerely,</p>
      <div class="signature" role="img" aria-label="Handwritten signature"></div>
      <p>Ruth Benning<br><span class="muted">Attorney</span></p>
    </div>
    <svg class="band" viewBox="0 0 340 70" preserveAspectRatio="none" aria-hidden="true">
      <polygon points="0,22 340,0 340,70 0,70" fill="var(--navy)"/>
      <polygon points="0,18 340,-4 340,0 0,22" fill="var(--grey)"/>
    </svg>
    <div class="letter-footer">2847 Tamworth Lane, Suite 3405, Kennesaw, GA 30582<br>T (770) 555-0142 · ruthbenningesq@quillpost.net · www.marlowelegaloffice.com</div>
  </section>

  <!-- Fax cover -->
  <section class="sheet fax">
    <div class="brand"><span class="brand-dot"></span><span class="brand-name">The Marlowe Legal Group, P.C.</span></div>
    <div class="fax-title">FAX</div>
    <table class="fax-table">
      <tr><td class="label">To:</td><td></td></tr>
      <tr><td class="label">From:</td><td></td></tr>
      <tr><td class="label">Fax:</td><td></td></tr>
      <tr><td class="label">Pages:</td><td></td></tr>
      <tr><td class="label">Phone:</td><td></td></tr>
      <tr><td class="label">Date:</td><td></td></tr>
      <tr><td class="label">Re:</td><td></td></tr>
    </table>
    <div class="fax-checks"><span>Urgent</span><span>For Review</span><span>Please Comment</span><span>Please Reply</span></div>
    <div class="fax-comments">Comments:</div>
    <div class="fax-lines"></div>
    <div class="fax-footer">2847 Tamworth Lane, Suite 3405, Kennesaw, GA 30582 · T (770) 555-0142</div>
  </section>

  <!-- Envelope front -->
  <section class="sheet envelope-front">
    <div class="envelope-mark" aria-hidden="true"></div>
    <div class="brand"><span class="brand-dot"></span><span class="brand-name">The Marlowe Legal Group, P.C.</span></div>
    <p class="small">2847 Tamworth Lane<br>Suite 3405<br>Kennesaw, GA 30582</p>
  </section>

  <!-- Envelope back -->
  <section class="sheet envelope-back">
    <svg viewBox="0 0 400 230" preserveAspectRatio="none" aria-hidden="true">
      <polyline points="0,230 200,120 400,230" fill="none" stroke="var(--grey-light)" stroke-width="1"/>
      <path d="M0,0 H400 V40 Q300,70 200,125 Q100,70 0,40 Z" fill="var(--navy)"/>
    </svg>
    <span class="seal"></span>
  </section>

  <!-- Business card, front -->
  <section class="sheet card card-front card-1">
    <div class="brand"><span class="brand-dot"></span><span class="brand-name">The Marlowe Legal Group, P.C.</span></div>
    <div class="card-person">
      <h2>Ruth Benning</h2>
      <p>Attorney</p>
      <div class="small">2847 Tamworth Lane, Suite 3405<br>Kennesaw, GA 30582<br>T (770) 555-0142 · F (770) 555-0143<br>ruthbenningesq@quillpost.net</div>
    </div>
    <span class="card-stripe"></span>
  </section>

  <!-- Business card, navy back -->
  <section class="sheet card card-back card--navy card-2">
    <div class="brand brand--light"><span class="brand-dot"></span><span class="brand-name">The Marlowe Legal Group, P.C.</span></div>
    <div class="web">www.marlowelegaloffice.com</div>
  </section>

  <!-- Business card, front alt -->
  <section class="sheet card card-front card-3">
    <div class="brand"><span class="brand-dot"></span><span class="brand-name">The Marlowe Legal Group, P.C.</span></div>
    <div class="card-person">
      <h2>Ruth Benning</h2>
      <p>Attorney</p>
      <div class="small">2847 Tamworth Lane, Suite 3405<br>Kennesaw, GA 30582<br>www.marlowelegaloffice.com<br>ruthbenningesq@quillpost.net</div>
    </div>
    <span class="card-stripe"></span>
  </section>

  <!-- Business card, grey back -->
  <section class="sheet card card-back card--grey card-4">
    <div class="brand brand--light"><span class="brand-dot"></span><span class="brand-name">The Marlowe Legal Group, P.C.</span></div>
    <div class="web">www.marlowelegaloffice.com</div>
  </section>

</body>
</html>
```